Looking for a modern elegant home improvment website

Looking for a new Design on current website . Please us www.larkfieldbuilders.example PIctures of recent work and stock photos that were attached , Free estimates , Explaining what we do , Similiar to www. larkfieldbuilders.example which is our current webpage . Colors can be different . I have attached our buisness card as well as our postcard we send out to homes . I would like a modern web page that our costumers can feel is professional so they can have a feeling of trust when they hire us . Our address should be on there . Licenesed & Insured should be somewhere on the page . Our Company Logo should be there as well . It would be nice to have a very modern website with great pictures of home interiors and exteriors . a page describing what we do is very important . facebook link to our page is a must as well as a instagram .
Updates

Reason: Looking for a elegant modern 5 page website with proper spelling and professional looking . I extended the deadline and upgraded .

Reason: Looking for more design options .

Target Market(s)

Home owners , Commerical buisness,

Industry/Entity Type

Home Improvement

Number of Pages Required

5+ page

Font styles to use
Serif

Requirements
Must have
• PIctures of recent work and stock photos that were attached , Free estimates , Explaining what we do , Similiar to www. larkfieldbuilders.example which is our current webpage . Colors can be different . I have attached our buisness card as well as our postcard we send out to homes . I would like a modern web page that our costumers can feel is professional so they can have a feeling of trust when they hire us . Our address should be on there . Licenesed & Insured should be somewhere on the page . Our Company Logo should be there as well .
Nice to have
• It would be nice to have a very modern website with great pictures of home interiors and exteriors . a page describing what we do is very important . facebook link to our page is a must as well as a instagram .

```html
<!DOCTYPE html>
<html lang="en">
<head>
<meta charset="utf-8">
<title>Larkfield Builders LLC — We Build Better Spaces</title>
<link rel="stylesheet" href="https://fonts.googleapis.com/css2?family=Montserrat:wght@700;800&family=Playfair+Display:wght@400&display=swap">
<style>
  :root {
    --stage: #4a4a4a;
    --white: #ffffff;
    --white-soft: rgba(255,255,255,0.85);
    --ring: rgba(255,255,255,0.45);
    --photo-top: #b9b6b2;
    --photo-mid: #9e9186;
    --photo-low: #8a6a52;
    --photo-floor: #6e4a30;
    --shade: rgba(20,16,12,0.28);
  }
  * { margin: 0; padding: 0; box-sizing: border-box; }
  html, body {
    width: 1200px; height: 1200px; overflow: hidden;
    background: var(--stage);
  }
  .site {
    position: absolute; left: 0; top: 227px;
    width: 1200px; height: 746px; overflow: hidden;
  }
  .hero-photo {
    position: absolute; inset: 0;
    background:
      linear-gradient(90deg, rgba(235,220,205,0.35) 0%, rgba(0,0,0,0) 22%, rgba(0,0,0,0) 78%, rgba(235,220,205,0.35) 100%),
      linear-gradient(180deg, var(--photo-top) 0%, var(--photo-mid) 48%, var(--photo-low) 78%, var(--photo-floor) 100%);
  }
  .hero-shade { position: absolute; inset: 0; background: var(--shade); }
  .main-nav {
    position: absolute; top: 52px; left: 410px;
    display: flex; gap: 26px;
    font-family: "Montserrat", sans-serif; font-weight: 700;
    font-size: 11px; letter-spacing: 2.4px; text-transform: uppercase;
    color: var(--white);
  }
  .social-links {
    position: absolute; top: 51px; left: 981px;
    display: flex; gap: 32px;
  }
  .social-links span {
    width: 14px; height: 14px; border-radius: 50%;
    background: var(--white-soft); display: block;
  }
  .brand {
    position: absolute; top: 300px; left: 0; width: 1200px;
    display: flex; flex-direction: column; align-items: center;
  }
  .brand-name {
    font-family: "Playfair Display", serif; font-weight: 400;
    font-size: 20px; letter-spacing: 1.5px; text-transform: uppercase;
    color: var(--white); padding: 0 18px 8px;
    border-bottom: 2px solid var(--white);
  }
  .headline {
    position: absolute; top: 362px; left: 0; width: 1200px;
    text-align: center;
    font-family: "Montserrat", sans-serif; font-weight: 800;
    font-size: 48px; line-height: 57px; letter-spacing: -0.5px;
    color: var(--white);
  }
  .tagline {
    position: absolute; top: 497px; left: 0; width: 1200px;
    text-align: center;
    font-family: "Playfair Display", serif; font-weight: 400;
    font-size: 19px; line-height: 27px;
    color: var(--white-soft);
  }
  .slide-arrow {
    position: absolute; top: 378px;
    width: 70px; height: 70px; border-radius: 50%;
    border: 1px solid var(--ring);
    display: flex; align-items: center; justify-content: center;
  }
  .slide-arrow.prev { left: 110px; }
  .slide-arrow.next { left: 1017px; }
</style>
</head>
<body>
  <main class="site">
    <div class="hero-photo" role="img" aria-label="Sunlit loft interior with tall black-framed windows, sheer curtains, white radiators and a leather butterfly chair with a knit pillow"></div>
    <div class="hero-shade"></div>

    <nav class="main-nav">
      <span>Projects</span>
      <span>About Us</span>
      <span>Stories</span>
      <span>Contact</span>
    </nav>

    <div class="social-links" aria-label="Social links">
      <span></span><span></span><span></span>
    </div>

    <div class="brand">
      <div class="brand-name">Larkfield Builders LLC</div>
    </div>

    <h1 class="headline">We Build Better<br>Spaces</h1>
    <p class="tagline">Because your home is the most<br>important asset you have.</p>

    <div class="slide-arrow prev" aria-label="Previous slide">
      <svg width="32" height="20" viewBox="0 0 32 20"><path d="M31 10H2M11 1L2 10l9 9" fill="none" stroke="#fff" stroke-width="1.6"/></svg>
    </div>
    <div class="slide-arrow next" aria-label="Next slide">
      <svg width="32" height="20" viewBox="0 0 32 20"><path d="M1 10h29M21 1l9 9-9 9" fill="none" stroke="#fff" stroke-width="1.6"/></svg>
    </div>
  </main>
</body>
</html>
```